Business Card Design for Law firm - already have logo

Now that we have a logo, we need a business card design - our logo is attached -it is salaryman font if that helps - we would like a file that can be uploaded to cardquill (www.cardquill-example.com) using the logo and with the following information on it:
Quenby Law Firm, P.C.
Delwyn Quenby, Esq.
5817 SW 19th Ave.
Fernhollow, OR 97390
971.555.0142 phone
971.555.0187 fax
del@quenby-example.net
Voxline: delquenby
Chatwire: delwyn.quenby@mailbox-example.com
Target Market(s)
our business cards are distributed to corporate executives, technology professionals and healthcare providers
Industry/Entity Type
Business
Look and feel

```html
<!DOCTYPE html>
<html lang="en">
<head>
<meta charset="utf-8">
<title>Quenby Law Firm, P.C. — Business Card</title>
<link rel="stylesheet" href="https://fonts.googleapis.com/css2?family=Tinos&display=swap">
<style>
  :root {
    --frame: #000000;
    --card: #ffffff;
    --ink: #111111;
    --accent: #e8262a;
  }
  html, body {
    margin: 0;
    padding: 0;
    width: 1200px;
    height: 800px;
    overflow: hidden;
    background: var(--frame);
  }
  .card {
    position: relative;
    width: 1200px;
    height: 800px;
    background: var(--frame);
    font-family: "Tinos", "Times New Roman", serif;
    text-transform: uppercase;
  }
  .card-face {
    position: absolute;
    left: 22px;
    top: 32px;
    width: 1146px;
    height: 740px;
    background: var(--card);
  }
  .firm-name {
    position: absolute;
    left: 170px;
    top: 95px;
    width: 842px;
    height: 203px;
    display: flex;
    align-items: center;
    justify-content: center;
    font-size: 150px;
    letter-spacing: 28px;
    color: var(--ink);
    line-height: 1;
    padding-left: 28px;
    box-sizing: border-box;
  }
  .divider {
    position: absolute;
    left: 543px;
    top: 382px;
    width: 6px;
    height: 287px;
    background: var(--ink);
  }
  .contact-left {
    position: absolute;
    right: 683px;
    top: 425px;
    text-align: right;
  }
  .contact-right {
    position: absolute;
    left: 573px;
    top: 425px;
    text-align: left;
  }
  .line { margin: 0; line-height: 23px; font-size: 26px; color: var(--ink); white-space: nowrap; }
  .accent { color: var(--accent); }
  .person-name { font-size: 27px; line-height: 34px; margin-bottom: 16px; }
  .address { margin-bottom: 24px; }
  .email-main { font-size: 27px; line-height: 34px; margin-bottom: 37px; }
  .handle { margin-bottom: 22px; font-size: 27px; }
  .chat-address { font-size: 22px; line-height: 27px; }
</style>
</head>
<body>
  <div class="card">
    <div class="card-face"></div>

    <div class="firm-name">Quenby</div>

    <div class="contact-left">
      <p class="line accent person-name">Delwyn Quenby, Esq.</p>
      <div class="address">
        <p class="line">5817 SW 19th Ave.</p>
        <p class="line">Fernhollow, OR 97390</p>
      </div>
      <p class="line accent">971.555.0142 : Phone</p>
      <p class="line accent">971.555.0187 : Fax</p>
    </div>

    <div class="divider"></div>

    <div class="contact-right">
      <p class="line accent email-main">del@quenby-example.net</p>
      <p class="line handle"><span class="accent">Voxline:</span> delquenby</p>
      <p class="line accent">Chatwire:</p>
      <p class="line chat-address">delwyn.quenby@mailbox-example.com</p>
    </div>
  </div>
</body>
</html>
```